I need a flyer designed for a marine service company. Our company specializes in boat engine diagnostic/repair, engine service, electronic installation and repairs, bottom paint, detailing, winterization and shrink wrapping. We would like to see designs that incorporate our color scheme of deep blue, blueish gray and black (please see attached photo)

Target Market(s)

Boat owners

Industry/Entity Type

Marine

Logo Text

Kelpwick Harbor Marine Services

Requirements
Must have
• Company logo
Nice to have
• List the services we provide.

```html
<!DOCTYPE html>
<html lang="en">
<head>
<meta charset="utf-8">
<title>Kelpwick Harbor Marine Services – Flyer</title>
<link href="https://fonts.googleapis.com/css2?family=Cinzel:wght@500;600&family=Montserrat:wght@600;700&display=swap" rel="stylesheet">
<style>
  :root{
    --navy:#1c2a4a;
    --navy-deep:#14213d;
    --charcoal:#2b2f38;
    --sky-top:#8fb0d3;
    --sky-low:#c9d6e2;
    --white:#ffffff;
    --ink:#1a2440;
    --sea:#1f7f8c;
  }
  html,body{margin:0;padding:0;overflow:hidden;background:#fff;}
  .flyer{position:relative;width:900px;height:1200px;overflow:hidden;background:var(--white);font-family:"Montserrat",sans-serif;}
  .flyer-shapes{position:absolute;inset:0;}
  .brand{position:absolute;top:70px;left:0;width:100%;display:flex;justify-content:center;align-items:center;gap:12px;}
  .brand-dot{width:18px;height:18px;border-radius:50%;background:var(--navy);}
  .brand-name{font-family:"Cinzel",serif;font-weight:500;font-size:24px;color:var(--navy);letter-spacing:1px;}
  .headline{position:absolute;top:205px;left:0;width:100%;text-align:center;font-family:"Cinzel",serif;font-weight:600;line-height:1;margin:0;}
  .headline-top{display:block;font-size:62px;color:var(--white);letter-spacing:1px;}
  .headline-bottom{display:block;font-size:66px;color:var(--navy-deep);margin-top:6px;}
  .services-title{position:absolute;top:707px;left:34px;margin:0;font-weight:700;font-size:25px;letter-spacing:1.5px;color:var(--white);}
  .service-list{position:absolute;top:805px;left:32px;margin:0;padding:0;list-style:none;width:380px;}
  .service-item{display:flex;align-items:flex-start;gap:28px;height:47px;font-weight:700;font-size:17px;line-height:17px;color:var(--ink);}
  .service-item.tall{height:62px;}
  .service-icon{flex:none;width:32px;height:32px;margin-top:-7px;}
  .contact{position:absolute;right:36px;top:1052px;text-align:right;color:var(--white);}
  .contact-pill{display:inline-block;background:var(--white);color:var(--navy);font-weight:700;font-size:13px;letter-spacing:1px;padding:6px 16px;border-radius:16px;}
  .contact-phone{font-weight:700;font-size:28px;margin-top:10px;}
  .contact-mail{display:flex;align-items:center;justify-content:flex-end;gap:12px;font-weight:700;font-size:16px;margin-top:6px;}
</style>
</head>
<body>
<main class="flyer">
  <svg class="flyer-shapes" width="900" height="1200" viewBox="0 0 900 1200">
    <defs>
      <linearGradient id="heroFill" x1="0" y1="0" x2="0" y2="1">
        <stop offset="0" stop-color="#8fb0d3"/>
        <stop offset="0.42" stop-color="#c7d5e2"/>
        <stop offset="0.62" stop-color="#6f7f4e"/>
        <stop offset="0.75" stop-color="#4a6a7c"/>
        <stop offset="1" stop-color="#2e5a78"/>
      </linearGradient>
      <linearGradient id="seaFill" x1="0" y1="0" x2="1" y2="1">
        <stop offset="0" stop-color="#3aa0ae"/>
        <stop offset="1" stop-color="#17626f"/>
      </linearGradient>
      <linearGradient id="marinaFill" x1="0" y1="0" x2="0" y2="1">
        <stop offset="0" stop-color="#b9d0e2"/>
        <stop offset="1" stop-color="#6e9bb5"/>
      </linearGradient>
      <clipPath id="bigCircle"><circle cx="709" cy="848" r="150"/></clipPath>
      <clipPath id="smallCircle"><circle cx="526" cy="945" r="117"/></clipPath>
    </defs>

    <!-- hero scene -->
    <path role="img" aria-label="Photo of a large white and navy motor yacht anchored by a green wooded hillside under a pale blue sky"
          d="M0 0H900V640C640 710 320 700 0 620Z" fill="url(#heroFill)"/>
    <!-- navy swoosh under hero -->
    <path d="M0 620C320 700 640 710 900 640V660C640 730 320 725 0 650Z" fill="var(--navy)"/>
    <path d="M0 660C300 730 620 735 900 670V676C620 742 300 738 0 668Z" fill="var(--navy)"/>
    <!-- services band -->
    <path d="M0 668C120 696 240 712 370 717C330 745 250 768 0 772Z" fill="var(--charcoal)"/>

    <!-- round photos -->
    <g clip-path="url(#bigCircle)">
      <rect role="img" aria-label="Photo of a white superyacht cruising on turquoise open sea" x="559" y="698" width="300" height="300" fill="url(#seaFill)"/>
    </g>
    <circle cx="709" cy="848" r="150" fill="none" stroke="var(--navy)" stroke-width="3"/>
    <g clip-path="url(#smallCircle)">
      <rect role="img" aria-label="Photo of a white flybridge motor boat moored in a marina" x="409" y="828" width="234" height="234" fill="url(#marinaFill)"/>
    </g>
    <circle cx="526" cy="945" r="117" fill="none" stroke="var(--navy)" stroke-width="3"/>

    <!-- footer wave -->
    <path d="M0 1150C250 1150 450 1120 650 1060C740 1035 820 1022 900 1020V1200H0Z" fill="var(--navy)"/>
    <path d="M0 1130C250 1135 450 1105 640 1048C730 1022 820 1008 900 1006" fill="none" stroke="var(--navy)" stroke-width="5"/>
  </svg>

  <div class="brand">
    <span class="brand-dot"></span>
    <span class="brand-name">Kelpwick Harbor</span>
  </div>

  <h1 class="headline">
    <span class="headline-top">KELPWICK HARBOR</span>
    <span class="headline-bottom">MARINE SERVICES</span>
  </h1>

  <h2 class="services-title">OUR SERVICES</h2>

  <ul class="service-list">
    <li class="service-item">
      <svg class="service-icon" viewBox="0 0 32 32"><circle cx="16" cy="16" r="15" fill="var(--navy)"/><circle cx="16" cy="16" r="7" fill="none" stroke="#fff" stroke-width="2.5"/><path d="M16 6v20M6 16h20" stroke="#fff" stroke-width="2"/></svg>
      Boat engine diagnostic/repair
    </li>
    <li class="service-item">
      <svg class="service-icon" viewBox="0 0 32 32"><circle cx="16" cy="16" r="15" fill="var(--navy)"/><circle cx="16" cy="16" r="6" fill="none" stroke="#fff" stroke-width="3" stroke-dasharray="3 2"/><circle cx="16" cy="16" r="2" fill="#fff"/></svg>
      Engine service
    </li>
    <li class="service-item tall">
      <svg class="service-icon" viewBox="0 0 32 32"><circle cx="16" cy="16" r="15" fill="var(--navy)"/><rect x="9" y="10" width="14" height="11" rx="2" fill="none" stroke="#fff" stroke-width="2"/><path d="M12 24h8" stroke="#fff" stroke-width="2"/></svg>
      <span>Electronic installation and<br>repairs</span>
    </li>
    <li class="service-item">
      <svg class="service-icon" viewBox="0 0 32 32"><circle cx="16" cy="16" r="15" fill="var(--navy)"/><path d="M20 8l4 4-8 8-4-4z" fill="#fff"/><path d="M12 16l-4 8 8-4" fill="#fff"/></svg>
      Bottom paint
    </li>
    <li class="service-item">
      <svg class="service-icon" viewBox="0 0 32 32"><circle cx="16" cy="16" r="15" fill="var(--navy)"/><circle cx="16" cy="16" r="9" fill="none" stroke="#fff" stroke-width="1.8"/><circle cx="16" cy="16" r="5" fill="none" stroke="#fff" stroke-width="1.8"/></svg>
      Detailing
    </li>
    <li class="service-item tall">
      <svg class="service-icon" viewBox="0 0 32 32"><circle cx="16" cy="16" r="15" fill="var(--navy)"/><path d="M16 7v18M8.2 11.5l15.6 9M8.2 20.5l15.6-9" stroke="#fff" stroke-width="2"/></svg>
      <span>Winterization and shrink<br>wrapping</span>
    </li>
  </ul>

  <div class="contact">
    <span class="contact-pill">FOR MORE INFO</span>
    <div class="contact-phone">+1 555-018-2290</div>
    <div class="contact-mail">
      <svg width="20" height="14" viewBox="0 0 20 14"><rect x="0" y="0" width="20" height="14" fill="#fff"/><path d="M0 0l10 8 10-8" fill="none" stroke="var(--navy)" stroke-width="2"/></svg>
      kelpwickmarine@example.com
    </div>
  </div>
</main>
</body>
</html>
```